Corporate Two Sided Business Card

Looking for a Corporate "edgy" Modern look and feel for a business card

We are looking at two options. Dark background with our logo on it, white background with our logo on it - The background is more - Charcoal / Graphite then black

Details will be

Danielle Forsk

Licensee / Director

m. 0428 519 064

e. danielle@quorvela.com.au

quorvela.com.au

Target Market(s)

Professional Business people that refer use business and clients that own Investment Properties

Industry/Entity Type

Business

Contact Information for Business Card

Details will be

Danielle Forsk

Licensee / Director

m. 0428 519 064

quorvela.com.au

Font styles to use
Serif

Colors
000000
ec1f27
eeeeee
ffffff

Requirements
Must have
• Two options - White Background and Dark Background. - Two sided
Nice to have
• A design that is edgy, modern and new to look instead of boring style corporate cards - It should be a full integrated design
Should not have
• Block looking - Cheap.

```html
<!DOCTYPE html>
<html lang="en">
<head>
<meta charset="utf-8">
<title>Quorvela Business Card</title>
<link rel="stylesheet" href="https://fonts.googleapis.com/css2?family=Roboto:wght@400;500&family=Roboto+Condensed:wght@500;700&display=swap">
<style>
  :root {
    --stage: #2b2b2b;
    --paper: #f1f1f1;
    --ink: #4d4d4d;
    --red: #e11f26;
    --bar: #565656;
    --white: #ffffff;
    --tint: #f3dcdc;
  }
  * { margin: 0; padding: 0; box-sizing: border-box; }
  html, body { width: 1200px; height: 960px; overflow: hidden; }
  body { background: var(--stage); position: relative; font-family: "Roboto", Arial, sans-serif; }

  .card {
    position: absolute;
    width: 600px;
    height: 343px;
    background: var(--paper);
    overflow: hidden;
  }
  .card--front { left: 314px; top: 113px; }
  .card--back { left: 311px; top: 472px; }

  .brand-name {
    position: absolute;
    font-family: "Roboto", Arial, sans-serif;
    font-weight: 500;
    color: var(--ink);
    line-height: 1;
  }
  .card--front .brand-name { right: 48px; top: 56px; font-size: 44px; }

  .name-band { position: absolute; left: 0; top: 238px; width: 330px; height: 60px; }
  .name-band svg { display: block; }
  .person {
    position: absolute;
    left: 36px;
    top: 246px;
    color: var(--white);
    font-family: "Roboto Condensed", "Arial Narrow", sans-serif;
    line-height: 1;
  }
  .person__name { font-size: 21px; font-weight: 700; letter-spacing: 0.2px; }
  .person__role { font-size: 16px; font-weight: 500; margin-top: 5px; letter-spacing: 0.3px; }

  .contact-bar {
    position: absolute;
    left: 0; bottom: 0;
    width: 100%; height: 43px;
    background: var(--bar);
    display: flex;
    align-items: center;
    padding-left: 35px;
    gap: 9px;
    color: var(--white);
    font-size: 14.5px;
  }
  .contact-item { display: flex; align-items: center; gap: 5px; white-space: nowrap; }
  .contact-item svg { fill: var(--white); flex: none; }

  .brand-tile {
    position: absolute;
    left: 17px; top: 80px;
    width: 246px; height: 246px;
    background: var(--tint);
  }
  .card--back .brand-name { right: 38px; top: 251px; font-size: 40px; }
  .brand-url {
    position: absolute;
    right: 36px; top: 292px;
    font-size: 15px;
    letter-spacing: 3.2px;
    color: var(--ink);
  }
</style>
</head>
<body>
  <section class="card card--front">
    <div class="brand-name">Quorvela</div>

    <div class="name-band">
      <svg width="330" height="60" viewBox="0 0 330 60"><polygon points="0,0 264,0 324,59 0,59" fill="var(--red)"/></svg>
    </div>
    <div class="person">
      <div class="person__name">DANIELLE FORSK</div>
      <div class="person__role">LICENSEE / DIRECTOR</div>
    </div>

    <div class="contact-bar">
      <span class="contact-item">
        <svg width="10" height="16" viewBox="0 0 10 16"><path d="M1.5 0h7A1.5 1.5 0 0 1 10 1.5v13A1.5 1.5 0 0 1 8.5 16h-7A1.5 1.5 0 0 1 0 14.5v-13A1.5 1.5 0 0 1 1.5 0zM1.5 2v10.5h7V2zM5 13.3a.9.9 0 1 0 0 1.8.9.9 0 0 0 0-1.8z"/></svg>
        0428 519 064
      </span>
      <span class="contact-item">
        <svg width="14" height="10" viewBox="0 0 14 10"><path d="M0 0h14v1L7 5.5 0 1zM0 2.3l7 4.5 7-4.5V10H0z"/></svg>
        danielle@quorvela.com.au
      </span>
      <span class="contact-item">
        <svg width="14" height="14" viewBox="0 0 14 14"><circle cx="7" cy="7" r="7"/><path d="M4 3.5c1.5.3 2 1.3 1.3 2.3-.7.9.6 1.7 1.6 1.4.9 1.3-.4 2.6.3 3.8M9.5 3c-.6.9.2 1.6 1.3 1.6" stroke="var(--bar)" stroke-width="1.3" fill="none"/></svg>
        www.quorvela.com.au
      </span>
    </div>
  </section>

  <section class="card card--back">
    <div class="brand-tile"></div>
    <div class="brand-name">Quorvela</div>
    <div class="brand-url">www.quorvela.com.au</div>
  </section>
</body>
</html>
```